Meridell Associates brouchure

I am attaching a sample of what I would like to be created in a vector format or format that I can send to a printer.

The Meridell Associates logo is the style I like.

Thanks, Gus

Industry/Entity Type

Printer

Font styles to use
Other font styles liked:
• please see attached

Requirements
Must have
• please create a format that I can provide to a printer for making a brochure
• UPDATE: please if possible, have the size be 10'' wide by 11'' tall
• with the brochure opening from top to bottom like a calendar
Nice to have
• I like where you are going with this, can you put an image on the top of the page and the text on the bottom of the page
• when you are holding the marketing piece, it should be 10'' wide by 5.5'' tall, after you open the cover page, then it becomes 10'' wide by 11'' tall
• the top page is an image and the lower page is the message..
• so when you view it you see a picture and then text
• the front cover should have the logo image -
• Meridell Associates
• the wording - cost effective resources for your practice
• cash back medical plans, 15% medical wellness discount
• on the inside pages 1-3 keep the tag line Meridell Associates / Practice Management
• the contact info on page 4
• the last page - Meridell Associates logo in the middle, then Practice Management on the bottom

```html
<!DOCTYPE html>
<html lang="en">
<head>
<meta charset="utf-8">
<title>Meridell Associates – Tent Brochure Flat</title>
<link href="https://fonts.googleapis.com/css2?family=Open+Sans:ital,wght@0,400;0,600;0,700;1,600;1,700&display=swap" rel="stylesheet">
<style>
  :root{
    --charcoal:#3f4043;
    --brand-blue:#3a86cf;
    --paper:#ffffff;
    --ink:#2b2b2b;
    --mist-1:#f4f5f6;
    --mist-2:#e3e5e8;
    --photo-dark:#2e3340;
    --photo-mid:#9aa3ad;
    --photo-light:#eef0f2;
  }
  *{box-sizing:border-box;margin:0;padding:0}
  html,body{width:1200px;height:1200px;overflow:hidden;background:#ffffff}
  body{font-family:"Open Sans",Arial,sans-serif;color:var(--ink)}

  .sheet{
    position:absolute;left:100px;top:50px;width:1000px;height:1100px;
    background:var(--paper);
    box-shadow:0 14px 22px rgba(0,0,0,.35);
    overflow:hidden;
  }

  /* ---------- back panel (prints upside down) ---------- */
  .panel-back{
    position:absolute;left:0;top:0;width:1000px;height:540px;
    transform:rotate(180deg);
  }
  .back-logo-band{
    position:absolute;left:0;top:0;width:100%;height:120px;
    background:var(--charcoal);
    display:flex;align-items:center;justify-content:center;
  }
  .back-rule{position:absolute;left:0;top:120px;width:100%;height:6px;background:var(--brand-blue)}
  .back-message{position:absolute;left:0;top:126px;width:100%;height:320px}
  .back-message .faded-photo{
    position:absolute;inset:0;
    background:linear-gradient(100deg,var(--mist-1) 0%,var(--mist-2) 35%,#f7f7f8 60%,var(--mist-2) 100%);
  }
  .back-message .copy{
    position:absolute;left:0;right:0;top:140px;
    text-align:center;font-size:15px;line-height:22px;color:#333;
  }
  .back-message .copy p+p{margin-top:10px}
  .back-contact-band{position:absolute;left:0;bottom:0;width:100%;height:94px}
  .back-contact-band svg.band{position:absolute;inset:0}
  .contact-list{
    position:absolute;left:380px;top:18px;
    display:grid;grid-template-columns:auto auto;column-gap:56px;row-gap:6px;
    color:#fff;font-size:15px;line-height:22px;
  }
  .contact-item{display:flex;align-items:center;gap:10px}
  .contact-item svg{flex:none}

  /* ---------- front cover ---------- */
  .panel-front{position:absolute;left:0;top:540px;width:1000px;height:560px}
  .front-header{position:absolute;left:0;top:0;width:100%;height:108px}
  .front-header svg.tab{position:absolute;left:0;top:16px}
  .tagline{
    position:absolute;left:34px;top:16px;height:86px;
    display:flex;align-items:center;
    color:#fff;font-style:italic;font-weight:600;font-size:25px;letter-spacing:.2px;
  }
  .brand-name{
    font-family:"Open Sans",Arial,sans-serif;font-weight:700;
    line-height:1;text-align:center;
  }
  .front-header .brand-name{
    position:absolute;right:50px;top:20px;color:var(--brand-blue);font-size:34px;
  }
  .back-logo-band .brand-name{color:#fff;font-size:40px}
  .front-photo{
    position:absolute;left:0;top:108px;width:100%;height:368px;
    background:
      radial-gradient(ellipse at 30% 70%,#f4f5f7 0%,#e6e8eb 35%,transparent 60%),
      linear-gradient(90deg,#3a3430 0%,#c9c3bd 20%,#eceef0 45%,#8d96a2 70%,var(--photo-dark) 100%);
  }
  .front-footer{position:absolute;left:0;top:478px;width:100%;height:72px}
  .front-footer svg{position:absolute;inset:0}
  .offer{
    position:absolute;left:195px;top:0;height:72px;right:30px;
    display:flex;align-items:center;justify-content:center;gap:8px;
    color:#fff;font-weight:600;font-size:22px;letter-spacing:.2px;white-space:nowrap;
  }
  .offer .figure{font-size:32px;font-weight:600}
</style>
</head>
<body>
<main class="sheet">

  <section class="panel-back">
    <header class="back-logo-band">
      <div class="brand-name">Meridell<br>Associates</div>
    </header>
    <div class="back-rule"></div>

    <div class="back-message">
      <div class="faded-photo" role="img" aria-label="Faint background photo of a hand holding a pen over documents"></div>
      <div class="copy">
        <p>Meridell Associates Practice Management is a relationship that gives your<br>practice time, cost and rewards.</p>
        <p>Proven guidance in group benefits, payroll, human resources, workers<br>compensation, 401(k) and more</p>
      </div>
    </div>

    <footer class="back-contact-band">
      <svg class="band" width="1000" height="94" viewBox="0 0 1000 94">
        <rect width="1000" height="94" fill="var(--charcoal)"/>
        <polygon points="0,0 185,0 140,94 0,94" fill="var(--brand-blue)"/>
        <polygon points="185,0 196,0 151,94 140,94" fill="var(--paper)"/>
      </svg>
      <div class="contact-list">
        <div class="contact-item">
          <svg width="16" height="18" viewBox="0 0 16 18"><circle cx="8" cy="10" r="7" fill="#fff"/><circle cx="8" cy="10" r="3" fill="var(--charcoal)"/></svg>
          <span>PO BOX 550912</span>
        </div>
        <div class="contact-item">
          <svg width="16" height="18" viewBox="0 0 16 18"><path d="M3 2h4l1 4-2 1.5c1 2 2.5 3.5 4.5 4.5L12 10l4 1v4c0 1-1 2-2 2C7 17 1 11 1 4c0-1 1-2 2-2z" fill="#fff"/></svg>
          <span>555-014-2870</span>
        </div>
        <div class="contact-item">
          <span style="width:16px;display:inline-block"></span>
          <span>LAKE ORLEN FL 32914</span>
        </div>
        <div class="contact-item">
          <svg width="16" height="16" viewBox="0 0 16 16"><rect x="1" y="2" width="14" height="10" rx="1" fill="none" stroke="#fff" stroke-width="1.6"/><rect x="5" y="13" width="6" height="2" fill="#fff"/></svg>
          <span>www.meridellassoc.com</span>
        </div>
      </div>
    </footer>
  </section>

  <section class="panel-front">
    <header class="front-header">
      <svg class="tab" width="640" height="86" viewBox="0 0 640 86">
        <polygon points="0,0 594,0 634,86 0,86" fill="var(--brand-blue)"/>
      </svg>
      <div class="tagline">Cost Effective Resources For Your Practice</div>
      <div class="brand-name">Meridell<br>Associates</div>
    </header>

    <div class="front-photo" role="img" aria-label="Photo of a professional's hand pointing a pen at a financial chart on paper"></div>

    <footer class="front-footer">
      <svg width="1000" height="72" viewBox="0 0 1000 72">
        <rect width="1000" height="72" fill="var(--charcoal)"/>
        <polygon points="0,0 190,0 150,72 0,72" fill="var(--brand-blue)"/>
        <polygon points="190,0 201,0 161,72 150,72" fill="var(--paper)"/>
      </svg>
      <div class="offer">
        <span>CASH BACK MEDICAL PLANS</span>
        <span class="figure">15%</span>
        <span>WELLNESS MEDICAL DISCOUNT</span>
      </div>
    </footer>
  </section>

</main>
</body>
</html>
```